High-end construction company needs a business card design

We need a modern looking business card that draws people in, is memorable and looks so good people will want to sick it on their fridges.
On the first side what is needed are:
Logo
My name - Tomas Verbelk
Title - Managing Director
Website - www.kravel.co.uk
Email - tomas@kravel.co.uk
Telephone - 020 5194 6381
Mobile - 07845319027
On the back side was is needed is a list of all the services we provide:
-Kitchen Renovations
-Bathroom Renovations
-House Renovations
-Garage Conversions
-Extensions
-Loft Conversions
-Conservatories
-Carpentry
-Tiling
-Electrical
-Plumbing & Heating
-Bricklaying
-Landscaping
-Decorating
-Plastering
We would like the colours to be the same shades as on the logo with grey or black for the words.
Target Market(s)
Anyone who needs building work done
Contact Information for Business Card
This business card is for a construction company which strives to deliver excellent service and quality.
The look and feel of the card should represent this.
Requirements
Must have
- On the first side what is needed are:
Logo
My name - Tomas Verbelk
Title - Managing Director
Website - www.kravel.co.uk
Email - tomas@kravel.co.uk
Telephone - 020 5194 6381
Mobile - 07845319027
Nice to have
- Cool looking features

```html
<!DOCTYPE html>
<html lang="en">
<head>
<meta charset="utf-8">
<title>Kravel Construction Ltd — Business Card</title>
<link href="https://fonts.googleapis.com/css2?family=Arimo:wght@400;700&display=swap" rel="stylesheet">
<style>
  :root {
    --page-bg: #efefef;
    --card-dark: #393a3a;
    --card-light: #f8f8f8;
    --green-dark: #4a8c40;
    --green-mid: #5aa63c;
    --green-light: #72bd42;
    --lime: #b5d334;
    --text-light: #f2f2f2;
    --text-muted: #d8d8d8;
    --text-dark: #333333;
  }
  * { margin: 0; padding: 0; box-sizing: border-box; }
  html, body {
    width: 1200px; height: 1200px; overflow: hidden;
    background: var(--page-bg);
    font-family: "Arimo", Arial, sans-serif;
  }
  .canvas { position: relative; width: 1200px; height: 1200px; }

  .card { position: absolute; overflow: hidden; }
  .card--front { left: 208px; top: 109px; width: 767px; height: 447px; background: var(--card-dark); }
  .card--back { left: 208px; top: 620px; width: 769px; height: 446px; background: var(--card-light); }

  .accent-bar { position: absolute; top: 166px; width: 7px; height: 78px; background: var(--lime); }
  .accent-bar--left { left: 0; }
  .accent-bar--right { right: 0; }

  .brand {
    position: absolute; left: 0; right: 0; text-align: center;
    color: var(--green-mid); font-weight: 700;
  }
  .brand__mark {
    display: inline-block; width: 14px; height: 14px; background: var(--green-mid);
    margin-right: 10px; vertical-align: 6px;
  }
  .brand__name { font-size: 42px; letter-spacing: 1px; line-height: 1; }
  .brand__tagline { display: block; font-size: 11px; letter-spacing: 2.2px; margin-top: 6px; text-transform: uppercase; }
  .card--front .brand { top: 118px; }
  .card--back .brand { top: 96px; }
  .card--back .brand__name { font-size: 40px; }

  .person { position: absolute; top: 211px; left: 0; right: 0; text-align: center; }
  .person__name {
    font-size: 22px; font-weight: 700; letter-spacing: 1px; text-transform: uppercase;
    color: var(--green-mid);
  }
  .person__first { color: var(--green-dark); }
  .person__title { font-size: 13px; color: var(--text-light); margin-top: 2px; letter-spacing: 0.3px; }

  .contact { position: absolute; top: 286px; left: 0; right: 0; text-align: center; color: var(--text-light); }
  .contact__phones { font-size: 15px; letter-spacing: 0.6px; }
  .contact__email { font-size: 12px; color: var(--text-muted); margin-top: 9px; letter-spacing: 0.3px; }

  .website {
    position: absolute; bottom: 11px; left: 0; right: 0; text-align: center;
    font-size: 11px; letter-spacing: 6.2px; color: var(--text-muted);
  }

  .services-heading {
    position: absolute; left: 25px; top: 195px;
    font-size: 14px; font-weight: 700; letter-spacing: 1.6px; color: var(--text-dark);
  }
  .services {
    position: absolute; top: 223px; height: 223px;
    padding: 41px 0 0 24px; color: #ffffff;
    font-size: 15px; letter-spacing: 1.6px; line-height: 27.5px; list-style: none;
  }
  .services--primary { left: 0; width: 389px; background: var(--green-dark); }
  .services--secondary { left: 389px; width: 380px; background: var(--green-light); padding-left: 22px; }
</style>
</head>
<body>
<main class="canvas">

  <section class="card card--front" aria-label="Business card front">
    <span class="accent-bar accent-bar--left"></span>
    <span class="accent-bar accent-bar--right"></span>

    <div class="brand">
      <span class="brand__name"><span class="brand__mark"></span>KRAVEL</span>
      <span class="brand__tagline">Construction Ltd</span>
    </div>

    <div class="person">
      <h1 class="person__name"><span class="person__first">Tomas</span> Verbelk</h1>
      <p class="person__title">Managing Director</p>
    </div>

    <div class="contact">
      <p class="contact__phones">020 5194 6381 &nbsp;, 07845319027</p>
      <p class="contact__email">tomas@kravel.co.uk</p>
    </div>

    <p class="website">www.kravel.co.uk</p>
  </section>

  <section class="card card--back" aria-label="Business card back">
    <div class="brand">
      <span class="brand__name"><span class="brand__mark"></span>KRAVEL</span>
      <span class="brand__tagline">Construction Ltd</span>
    </div>

    <h2 class="services-heading">Our Services</h2>

    <ul class="services services--primary">
      <li>-Carpentry &nbsp;-Tiling -Electrical</li>
      <li>-Plumbing &amp; Heating -Bricklaying</li>
      <li>-Landscaping -Decorating</li>
      <li>-Bathroom Renovations</li>
    </ul>
    <ul class="services services--secondary">
      <li>-Kitchen Renovations &nbsp;-Plastering</li>
      <li>-House Renovations -Conservatories</li>
      <li>-Garage Conversions</li>
      <li>-Extensions-Loft Conversions</li>
    </ul>
  </section>

</main>
</body>
</html>
```